Meadowtail Pet Business Card

We need a business card designed with two sides to it. I would like the front of the card to be mostly graphic and the back of the card to have the bullet points of our pet food.

I don't have a telephone number for the business yet so just leave a space for a toll free number. (800) xxx-xxxx.

Thanks,

Tobias

Combination Diet
Chicken Diet
Beef Diet
Lamb Diet

Website:  www.meadowtailpet-example.net

email:  rwelby@meadowtailpet-example.net

Direct - 347-xxx-xxxx
Toll Free - xxx-xxx-xxxx

www.meadowtailpet-example.net

Ravi Welby (Example)
Customer Experience Officer

rwelby@meadowtailpet-example.net
Direct - (347) xxx-xxxx

Sales Inquiries - (800) xxx-xxxx

All,

Please include the following items on the back of the business card.

Combination Diet
Chicken Diet
Beef Diet
Lamb Diet
 

Thanks,

Tobias

All, I will also want a QR code on the front or back of the card that can be scanned by a smart phone with our individual contact information.  Thanks, Tobias

Industry/Entity Type

Pet

```html
<!DOCTYPE html>
<html lang="en">
<head>
<meta charset="utf-8">
<title>Meadowtail Pet – Business Card</title>
<link href="https://fonts.googleapis.com/css2?family=Didact+Gothic&display=swap" rel="stylesheet">
<style>
  :root {
    --page: #e4e2df;
    --card-back: #b9523f;
    --ink-dark: #2a1a16;
    --ink-light: #fbeee6;
    --photo-deep: #3c4a24;
    --photo-meat: #a3473f;
    --photo-veg: #5f8a2f;
    --photo-carrot: #d9692a;
    --brand-light: #fff6e8;
  }
  * { box-sizing: border-box; margin: 0; padding: 0; }
  html, body { width: 1200px; height: 1200px; overflow: hidden; }
  body {
    background: var(--page);
    font-family: "Didact Gothic", "Century Gothic", sans-serif;
    position: relative;
  }
  .card {
    position: absolute;
    left: 110px;
    width: 980px;
    height: 560px;
    box-shadow: 0 6px 18px rgba(0,0,0,.25);
    overflow: hidden;
  }
  .card--front { top: 30px; }
  .card--back { top: 610px; background: var(--card-back); }

  .food-photo {
    position: absolute; inset: 0;
    background:
      radial-gradient(circle at 72% 30%, rgba(242,196,106,.9) 0 8%, transparent 14%),
      radial-gradient(ellipse at 62% 58%, var(--photo-meat) 0 14%, transparent 26%),
      radial-gradient(ellipse at 88% 55%, #d89a8f 0 10%, transparent 20%),
      radial-gradient(ellipse at 30% 78%, #e6d3cc 0 12%, transparent 22%),
      radial-gradient(ellipse at 85% 20%, var(--photo-carrot) 0 6%, transparent 14%),
      linear-gradient(135deg, var(--photo-veg), var(--photo-deep) 60%, #2e3a1c);
  }
  .brand-name {
    position: absolute;
    left: 90px; top: 200px;
    font-size: 64px;
    color: var(--brand-light);
    letter-spacing: .5px;
    text-shadow: none;
  }

  .entrees { position: absolute; left: 70px; top: 90px; color: var(--ink-dark); }
  .entrees__title { font-size: 35px; margin-bottom: 8px; }
  .entrees__list { list-style: none; color: var(--ink-light); font-size: 28px; }
  .entrees__list li { display: flex; align-items: center; gap: 12px; height: 42px; margin-left: 4px; }
  .entrees__list svg { width: 24px; height: 24px; fill: var(--ink-dark); }

  .back-brand {
    position: absolute; left: 140px; top: 400px;
    width: 230px; text-align: center;
    font-size: 30px; color: var(--ink-dark);
  }

  .contact-person { position: absolute; left: 500px; top: 85px; width: 400px; text-align: center; }
  .contact-person__name { font-size: 37px; color: var(--ink-light); }
  .contact-person__title { font-size: 26px; color: var(--ink-dark); margin-top: 4px; }

  .contact-details { position: absolute; left: 515px; top: 270px; font-size: 26px; }
  .contact-details .online { color: var(--ink-light); }
  .contact-details .online div { display: flex; align-items: center; gap: 12px; height: 36px; }
  .contact-details svg { width: 22px; height: 22px; }
  .contact-details .phones { color: var(--ink-dark); margin-top: 6px; }
  .contact-details .phones div { height: 41px; display: flex; align-items: flex-end; }
  .blank {
    display: inline-block; border-bottom: 2px solid var(--ink-dark);
    margin-left: 10px; margin-bottom: 8px;
  }
  .blank--3 { width: 64px; }
  .blank--4 { width: 82px; }
</style>
</head>
<body>
  <section class="card card--front">
    <div class="food-photo" role="img" aria-label="Photograph of raw meats, poultry, organ meat, apples, carrots, green beans and leafy greens"></div>
    <div class="brand-name">Meadowtail Pet</div>
  </section>

  <section class="card card--back">
    <div class="entrees">
      <h2 class="entrees__title" style="font-weight:400">Pet Food Entrées</h2>
      <ul class="entrees__list">
        <li><svg viewBox="0 0 24 24"><path d="M12 1l3.1 7 7.6.7-5.8 5 1.8 7.5L12 17.3 5.3 21.2l1.8-7.5-5.8-5 7.6-.7z"/></svg>Combination Diet</li>
        <li><svg viewBox="0 0 24 24"><path d="M12 1l3.1 7 7.6.7-5.8 5 1.8 7.5L12 17.3 5.3 21.2l1.8-7.5-5.8-5 7.6-.7z"/></svg>Chicken Diet</li>
        <li><svg viewBox="0 0 24 24"><path d="M12 1l3.1 7 7.6.7-5.8 5 1.8 7.5L12 17.3 5.3 21.2l1.8-7.5-5.8-5 7.6-.7z"/></svg>Beef Diet</li>
        <li><svg viewBox="0 0 24 24"><path d="M12 1l3.1 7 7.6.7-5.8 5 1.8 7.5L12 17.3 5.3 21.2l1.8-7.5-5.8-5 7.6-.7z"/></svg>Lamb Diet</li>
      </ul>
    </div>

    <div class="back-brand">Meadowtail Pet</div>

    <div class="contact-person">
      <div class="contact-person__name">Ravi Welby</div>
      <div class="contact-person__title">Customer Experience Officer</div>
    </div>

    <div class="contact-details">
      <div class="online">
        <div><svg viewBox="0 0 24 24"><circle cx="12" cy="12" r="11" fill="#2a1a16"/><rect x="6" y="8" width="12" height="8" fill="none" stroke="#b9523f" stroke-width="1.6"/><path d="M6 8l6 5 6-5" fill="none" stroke="#b9523f" stroke-width="1.6"/></svg>rwelby@meadowtailpet-example.net</div>
        <div><svg viewBox="0 0 24 24"><circle cx="12" cy="12" r="11" fill="#2a1a16"/><g fill="none" stroke="#b9523f" stroke-width="1.4"><circle cx="12" cy="12" r="7"/><ellipse cx="12" cy="12" rx="3" ry="7"/><path d="M5 12h14"/></g></svg>www.meadowtailpet</div>
      </div>
      <div class="phones">
        <div>Direct-(347)<span class="blank blank--3"></span><span class="blank blank--4"></span></div>
        <div>Toll Free<span class="blank blank--3"></span><span class="blank blank--4"></span></div>
        <div>Sales Inquiries:</div>
        <div>(800)<span class="blank blank--3"></span><span class="blank blank--3"></span><span class="blank blank--4"></span></div>
      </div>
    </div>
  </section>
</body>
</html>
```